Mental Health

QRT HAVEN
Behavioral Health
4172 W. Pell St. Mesa, AZ 85219
Gwendolyn (480)555-0142 / Omar 480-555-0187

Email: QRTHaven@Mailvex.example
Newly Remodeled & Spacious
g Staff
Registered Nurses
Licensed Independent &
Professional Substance &
Abuse Counselors
Behavioral Health Techs
Certified Caregivers
Behavioral Health &
Substance Abuse Professionals

To Refer a Patient
About Us
QRT Haven is a Fully Staffed Behavioral
Health Residential Facility, providing
treatment plans for adults suffering
with various Behavioral Health and
Substance Abuse disorders, while living
in a nice safe, clean and supportive
environment. Our home offers clients the
ability to learn the necessary skills to
help clients adapt, build self confidence
as well as independence, with the goal
of reducing the probability of a future
crisis or possible relapse. We offer
counseling programs, consisting of a
variety of addiction and recovery support
groups, independent living, coping and
social skills groups, as well as assisting
clients with using tools to create a resume
to help obtain employment and so much
more. We are committed to teaching
self management care and allowing
clients to understand how to utilize the
resources, skills and tools available for
long term success by providing superior
quality, all-inclusive living arrangements
and treatment options.

Thank you for your patience while I update the final content needed for us to make the final decision this week.

```html
<!DOCTYPE html>
<html lang="en">
<head>
<meta charset="utf-8">
<title>QRT Haven – Business Card</title>
<link rel="stylesheet" href="https://fonts.googleapis.com/css2?family=Quicksand:wght@400;500;600&display=swap">
<style>
  :root {
    --page-bg: #e9e6e1;
    --card-white: #f4f5f6;
    --brand-blue: #0a8fd0;
    --brand-blue-deep: #0769b0;
    --brand-green: #8cc23f;
    --text-white: #ffffff;
    --shadow: rgba(30, 40, 60, 0.22);
  }
  * { box-sizing: border-box; margin: 0; padding: 0; }
  html, body {
    width: 1200px;
    height: 780px;
    overflow: hidden;
    background: var(--page-bg);
    font-family: "Quicksand", sans-serif;
  }
  .canvas {
    position: relative;
    width: 1200px;
    height: 780px;
  }
  .card {
    position: absolute;
    top: 240px;
    width: 520px;
    height: 300px;
    border-radius: 18px;
    overflow: hidden;
    box-shadow: 0 14px 30px var(--shadow);
  }
  .card--front { left: 50px; background: var(--card-white); }
  .card--back {
    left: 630px;
    background: radial-gradient(ellipse at 45% 35%, #1aa3e2 0%, var(--brand-blue) 45%, var(--brand-blue-deep) 100%);
  }
  .card__waves { position: absolute; inset: 0; width: 100%; height: 100%; }

  .wordmark {
    position: absolute;
    display: flex;
    align-items: center;
    gap: 12px;
    font-weight: 500;
    letter-spacing: 3px;
    white-space: nowrap;
  }
  .wordmark__dot {
    border-radius: 50%;
    flex: none;
  }
  .card--front .wordmark { left: 28px; top: 34px; font-size: 24px; color: var(--brand-blue); }
  .card--front .wordmark__dot { width: 40px; height: 40px; background: var(--brand-green); }
  .card--back .wordmark {
    left: 50%; top: 50%;
    transform: translate(-50%, -50%);
    font-size: 38px;
    color: var(--text-white);
  }
  .card--back .wordmark__dot { width: 52px; height: 52px; border: 3px solid var(--text-white); }

  .address {
    position: absolute;
    right: 26px;
    top: 44px;
    color: var(--text-white);
    font-size: 13px;
    line-height: 1.4;
    text-align: right;
  }
  .contact {
    position: absolute;
    left: 160px;
    bottom: 26px;
    color: var(--text-white);
    font-size: 13px;
    line-height: 1.5;
  }
  .contact__name {
    font-size: 16px;
    letter-spacing: 1px;
    text-transform: uppercase;
    margin-bottom: 4px;
  }
  .contact__row { display: flex; align-items: center; gap: 8px; }
  .contact__icon {
    width: 16px; height: 16px;
    border-radius: 50%;
    background: var(--brand-green);
    display: flex; align-items: center; justify-content: center;
    flex: none;
  }
  .contact__icon svg { width: 10px; height: 10px; }
</style>
</head>
<body>
<main class="canvas">

  <section class="card card--front" aria-label="Business card front">
    <svg class="card__waves" viewBox="0 0 520 300" preserveAspectRatio="none" aria-hidden="true">
      <defs>
        <linearGradient id="blueFill" x1="0" y1="0" x2="1" y2="1">
          <stop offset="0" stop-color="#1aa3e2"/>
          <stop offset="1" stop-color="#0769b0"/>
        </linearGradient>
        <path id="waveEdge" d="M0,272 C70,266 110,230 140,196 C175,156 215,132 250,110 C285,88 305,72 330,60 C365,42 390,28 420,20 C460,10 490,4 520,0 L520,330 L0,330 Z"/>
      </defs>
      <use href="#waveEdge" transform="translate(0,-22)" fill="var(--brand-green)"/>
      <use href="#waveEdge" transform="translate(0,-8)" fill="var(--card-white)"/>
      <use href="#waveEdge" fill="url(#blueFill)"/>
    </svg>

    <div class="wordmark"><span class="wordmark__dot"></span>QRT HAVEN</div>

    <p class="address">4172 W. Pell St.<br>Mesa, AZ 85219</p>

    <div class="contact">
      <p class="contact__name">Gwendolyn</p>
      <p class="contact__row">
        <span class="contact__icon">
          <svg viewBox="0 0 10 10"><path d="M2,1 L4,1 L4.5,3 L3.4,3.8 C3.9,5 5,6.1 6.2,6.6 L7,5.5 L9,6 L9,8 C9,8.6 8.6,9 8,9 C4.5,9 1,5.5 1,2 C1,1.4 1.4,1 2,1 Z" fill="#fff"/></svg>
        </span>(480)555-0142
      </p>
      <p class="contact__row">
        <span class="contact__icon">
          <svg viewBox="0 0 10 10"><rect x="1" y="2.5" width="8" height="5.5" fill="#fff"/><path d="M1,2.5 L5,5.5 L9,2.5" stroke="#8cc23f" stroke-width="0.8" fill="none"/></svg>
        </span>QRTHaven@Mailvex.example
      </p>
    </div>
  </section>

  <section class="card card--back" aria-label="Business card back">
    <div class="wordmark"><span class="wordmark__dot"></span>QRT HAVEN</div>
  </section>

</main>
</body>
</html>
```